Merrow Sailcraft Works President Business Card Carbon fiber catamarans

Hi.. I need a new business card design.. I am the President of a high tech yacht builder. We build Carbon Fiber go fast catamarans... Maybe we use the file I am sharing to you as the back of the card.. We need to look cool and crisp ...

Target Market(s)

Affluent People who will purchase a cool yacht

Industry/Entity Type

Custom Yacht Builder

Contact Information for Business Card

Dale Penwarty , President, 517.608.2391 USA

Font styles to use
Serif

Requirements
Must have
• the clean crisp cool feel
Nice to have
• clean and crisp
Should not have
• Bold ugly

```html
<!DOCTYPE html>
<html lang="en">
<head>
<meta charset="utf-8">
<title>Merrow Sailcraft Works – Business Card</title>
<link rel="stylesheet" href="https://fonts.googleapis.com/css2?family=Oswald:wght@500&family=Poppins:wght@500;600&display=swap">
<style>
  :root {
    --navy: #0f1a2c;
    --white: #ffffff;
    --ink: #1b1f27;
    --steel: #5c6068;
    --ring: #b9bcc2;
    --backdrop: #3b4252;
  }
  * { margin: 0; padding: 0; box-sizing: border-box; }
  html, body { width: 1200px; height: 815px; overflow: hidden; }
  body {
    background: var(--backdrop);
    font-family: "Poppins", sans-serif;
    position: relative;
  }
  .card {
    position: absolute;
    top: 253px;
    width: 540px;
    height: 309px;
    border-radius: 4px;
    overflow: hidden;
    box-shadow: 0 12px 30px rgba(0,0,0,.35);
  }
  /* back side */
  .card-back { left: 40px; background: var(--navy); }
  .brand-back {
    position: absolute; inset: 0;
    display: flex; flex-direction: column; align-items: center; justify-content: center;
    color: var(--white);
    font-weight: 600;
    text-transform: uppercase;
    line-height: 1.1;
  }
  .brand-back .brand-main { font-size: 44px; letter-spacing: 10px; }
  .brand-back .brand-sub { font-size: 17px; letter-spacing: 7px; }

  /* front side */
  .card-front { left: 620px; background: var(--white); }
  .mark-spot {
    position: absolute; left: 34px; top: 72px;
    width: 110px; height: 110px; border-radius: 50%;
    border: 4px solid var(--ring);
    background: var(--white);
    z-index: 2;
  }
  .brand-front {
    position: absolute; right: 28px; top: 30px;
    text-align: right;
    color: var(--steel);
    font-weight: 600;
    text-transform: uppercase;
    line-height: 1.1;
  }
  .brand-front .brand-main { font-size: 24px; letter-spacing: 5px; }
  .brand-front .brand-sub { font-size: 11px; letter-spacing: 3px; }
  .name-band {
    position: absolute; left: 130px; right: 0; top: 112px; height: 98px;
    background: var(--navy);
    color: var(--white);
    text-align: right;
    padding: 10px 28px 0 0;
  }
  .person-name {
    font-family: "Oswald", sans-serif;
    font-weight: 500;
    font-size: 40px;
    letter-spacing: 1px;
    line-height: 1.1;
    text-transform: uppercase;
  }
  .person-title {
    font-weight: 600;
    font-size: 17px;
    letter-spacing: 2px;
    text-transform: uppercase;
    line-height: 1.3;
  }
  .contact-list {
    position: absolute; right: 28px; top: 224px;
    list-style: none;
    display: flex; flex-direction: column; gap: 5px;
  }
  .contact-item {
    display: flex; align-items: center; justify-content: flex-end; gap: 10px;
    color: var(--ink);
    font-size: 10px; font-weight: 600; line-height: 1.2;
    text-align: right;
  }
  .contact-icon {
    width: 22px; height: 22px; border-radius: 5px;
    background: var(--navy);
    display: flex; align-items: center; justify-content: center;
    flex: none;
  }
  .contact-icon svg { width: 13px; height: 13px; }
</style>
</head>
<body>

<section class="card card-back" aria-label="Card back">
  <div class="brand-back">
    <span class="brand-main">Merrow</span>
    <span class="brand-sub">Sailcraft Works</span>
  </div>
</section>

<section class="card card-front" aria-label="Card front">
  <div class="mark-spot" aria-hidden="true"></div>

  <div class="brand-front">
    <div class="brand-main">Merrow</div>
    <div class="brand-sub">Sailcraft Works</div>
  </div>

  <div class="name-band">
    <div class="person-name">Dale Penwarty</div>
    <div class="person-title">President</div>
  </div>

  <ul class="contact-list">
    <li class="contact-item">
      <span>517.608.2391</span>
      <span class="contact-icon">
        <svg viewBox="0 0 24 24" fill="none" stroke="#fff" stroke-width="2.4" stroke-linecap="round"><path d="M5 3h4l2 5-2.5 1.5a11 11 0 0 0 6 6L16 13l5 2v4a2 2 0 0 1-2 2A17 17 0 0 1 3 5a2 2 0 0 1 2-2z"/></svg>
      </span>
    </li>
    <li class="contact-item">
      <span>www.merrowsailcraft.com</span>
      <span class="contact-icon">
        <svg viewBox="0 0 24 24" fill="#fff"><path d="M21 3 3 10.5l7.5 3 3 7.5z"/></svg>
      </span>
    </li>
    <li class="contact-item">
      <span>118 Harbor Reach Rd. Lakeview,<br>South Carolina 29563, USA</span>
      <span class="contact-icon">
        <svg viewBox="0 0 24 24" fill="none" stroke="#fff" stroke-width="2.4"><path d="M12 22s7-7 7-12a7 7 0 0 0-14 0c0 5 7 12 7 12z"/><circle cx="12" cy="10" r="2.5"/></svg>
      </span>
    </li>
  </ul>
</section>

</body>
</html>
```